Etiketten für Karpatenkorn
Zielgruppe
Wir sind ein junges dynamisches Unternehmen aus Niederösterreich. Wir handeln mit Karpatenkorn aus den Karpaten. Neben Lecksteinen für Wild, Pferd, Nutz- und Haustiere handeln wir ebenfalls mit unbehandelten Speisesalz in Form von Steinsalz. Dieses haben wir natürlich oder mit Kräutern gemixt als Kräuter-Steinsalz (Wiesensalz) oder Badesalz. Unsere Zielgruppen sind also Jäger, Bauern, Landwirte, Zuchtställe als auch Haushalte für Kleintiere welche Salz benötigen (Hasen, Meerschweinchen usw..). Die persönlichen Zielgruppen sind Frauen als auch Männer.
Aufgabenstellung
Wir wünschen uns ein angenehm klares und helles Design. Es gibt ein bestehendes Design welches wir überarbeiten lassen möchten. Es wird für Runddosen, Drahtbügelgläser als auch für Kartonverpackungen verwendet.
Größe der Etiketten:
Streudose: 17x6cm
Etikett als Beilage& Drahtbügelglas: 12x7,5cm

```html
<!DOCTYPE html>
<html lang="de">
<head>
<meta charset="utf-8">
<title>Kräuter-Steinsalz Etikett</title>
<link href="https://fonts.googleapis.com/css2?family=Outfit:wght@300;600;700&family=Marcellus&display=swap" rel="stylesheet">
<style>
  :root {
    --page-bg: #ffffff;
    --label-bg: #f0f0ee;
    --diamond-light: #e6ecd6;
    --diamond-deep: #c5d4a3;
    --ink-dark: #2e3833;
    --ink-soft: #4e5752;
    --icon-green: #9cc64a;
    --icon-green-light: #cfe3a4;
    --sprig-tone: #b9c8a0;
  }
  * { margin: 0; padding: 0; box-sizing: border-box; }
  html, body {
    width: 1089px; height: 1200px; overflow: hidden;
    background: var(--page-bg);
  }
  .label {
    position: absolute; left: 314px; top: 150px;
    width: 461px; height: 900px;
    background: var(--label-bg);
    overflow: hidden;
    font-family: "Outfit", sans-serif;
  }
  .label__backdrop { position: absolute; inset: 0; }
  .brand {
    position: absolute; left: 0; right: 0; top: 176px;
    text-align: center;
    font-family: "Marcellus", serif;
    font-size: 27px; letter-spacing: 1px;
    color: var(--ink-soft);
  }
  .title {
    position: absolute; left: 0; right: 0; top: 312px;
    text-align: center;
    font-weight: 600; font-size: 53px; line-height: 70px;
    letter-spacing: 1px; color: var(--ink-dark);
  }
  .subtitle {
    position: absolute; left: 0; right: 0; top: 470px;
    text-align: center;
    font-weight: 300; font-size: 21px;
    color: var(--ink-soft);
  }
  .herb-sprig {
    position: absolute; left: 256px; top: 548px;
    width: 190px; height: 54px;
    border-radius: 27px;
    background: linear-gradient(90deg, var(--label-bg), var(--sprig-tone));
  }
  .crystal-badge { position: absolute; left: 73px; top: 560px; width: 250px; height: 245px; }
  .weight {
    position: absolute; left: 0; right: 0; top: 838px;
    text-align: center;
    font-weight: 700; font-size: 42px;
    color: #111;
  }
  .weight small { font-size: 26px; font-weight: 600; }
</style>
</head>
<body>
  <main class="label">
    <svg class="label__backdrop" width="461" height="900" viewBox="0 0 461 900" aria-hidden="true">
      <defs>
        <linearGradient id="diamondFill" x1="0" y1="0" x2="1" y2="1">
          <stop offset="0" stop-color="var(--diamond-light)"/>
          <stop offset="1" stop-color="var(--diamond-deep)"/>
        </linearGradient>
      </defs>
      <polygon points="230,24 650,444 230,864 -190,444" fill="url(#diamondFill)"/>
    </svg>

    <div class="brand">KARPATENKORN</div>

    <h1 class="title">KRÄUTER-<br>STEINSALZ</h1>
    <p class="subtitle">mit österreichischen Wiesenkräutern</p>

    <div class="herb-sprig" role="img" aria-label="Zeichnung eines Kräuterzweigs"></div>

    <svg class="crystal-badge" viewBox="0 0 250 245">
      <defs>
        <linearGradient id="badgeFill" x1="0" y1="1" x2="1" y2="0">
          <stop offset="0" stop-color="var(--icon-green)"/>
          <stop offset="1" stop-color="var(--icon-green-light)"/>
        </linearGradient>
      </defs>
      <rect x="68" y="10" width="170" height="170" rx="34" transform="rotate(45 153 95)" fill="url(#badgeFill)" opacity="0.9"/>
      <rect x="45" y="38" width="170" height="170" rx="34" transform="rotate(45 130 123)" fill="none" stroke="var(--ink-dark)" stroke-width="7"/>
      <rect x="70" y="70" width="110" height="105" rx="18" fill="var(--icon-green)" role="img" aria-label="Symbol eines Salzkristalls"/>
    </svg>

    <div class="weight">200 <small>g</small></div>
  </main>
</body>
</html>
```